Wine label for family vineyard start-up

Brand new family vineyard needs a new label:

The information we need on the label is the following:
- Merlot & Cabernet (variety)
- Ponte Valdora (location)
- 2016 (vintage)

The style of the label should be graphic / minimal / masculine.

This is a wine made by three 35yr old guys

Target Market(s)

young & urban

Industry/Entity Type

Vineyard

Logo Text

Merlot & Cabernet / Ponte Valdora / 2016

Font styles to use
Sans Serif

Requirements
Must have
• clearly legible
• aesthetically pleasing [minimalist]
• sans serif

```html
<!DOCTYPE html>
<html lang="en">
<head>
<meta charset="utf-8">
<title>Merlot / Cabernet 2016 – Wine Label</title>
<link rel="stylesheet" href="https://fonts.googleapis.com/css2?family=Questrial&family=Open+Sans:wght@400&display=swap">
<style>
  :root {
    --ink: #000000;
    --paper: #ffffff;
    --rule-dark: #9a9a9a;
    --rule-light: #b5b5b5;
    --vintage-grey: #8a8a8a;
    --label-font: "Questrial", sans-serif;
    --number-font: "Open Sans", sans-serif;
  }
  html, body {
    margin: 0;
    padding: 0;
    width: 915px;
    height: 1200px;
    overflow: hidden;
    background: var(--paper);
  }
  .canvas {
    position: relative;
    width: 915px;
    height: 1200px;
    background: var(--paper);
  }
  .label-sheet {
    position: absolute;
    left: 125px;
    top: 65px;
    width: 759px;
    height: 1107px;
    background: var(--ink);
  }
  .label-light {
    position: absolute;
    left: 134px;
    top: 611px;
    width: 734px;
    height: 527px;
    background: var(--paper);
  }
  .emblem {
    position: absolute;
  }
  .emblem--dark {
    left: 407px;
    top: 192px;
    width: 169px;
    height: 190px;
    background: radial-gradient(ellipse at center, #e6e6e6 0%, #bdbdbd 100%);
  }
  .emblem--light {
    left: 394px;
    top: 681px;
    width: 193px;
    height: 220px;
    background: radial-gradient(ellipse at center, #3a3a3a 0%, #111111 100%);
  }
  .variety, .location, .vintage {
    position: absolute;
    margin: 0;
    text-align: center;
    white-space: nowrap;
    line-height: 1;
  }
  .variety, .location {
    font-family: var(--label-font);
    font-weight: 400;
    letter-spacing: 0.04em;
  }
  .vintage {
    font-family: var(--number-font);
    font-weight: 400;
  }
  .rule {
    position: absolute;
    height: 1px;
  }

  /* dark variant */
  .dark .variety  { left: 303px; width: 396px; top: 405px; font-size: 35px; color: var(--paper); }
  .dark .rule     { left: 303px; width: 396px; top: 446px; background: var(--rule-dark); }
  .dark .location { left: 303px; width: 396px; top: 456px; font-size: 29px; color: var(--paper); }
  .dark .vintage  { left: 408px; width: 140px; top: 513px; font-size: 38px; color: var(--paper); }

  /* light variant */
  .light .variety  { left: 265px; width: 470px; top: 931px; font-size: 42px; color: var(--ink); }
  .light .rule     { left: 265px; width: 468px; top: 978px; background: var(--rule-light); }
  .light .location { left: 265px; width: 470px; top: 993px; font-size: 34px; color: var(--ink); }
  .light .vintage  { left: 395px; width: 160px; top: 1058px; font-size: 46px; color: var(--vintage-grey); }
</style>
</head>
<body>
  <main class="canvas">
    <div class="label-sheet"></div>

    <section class="dark">
      <div class="emblem emblem--dark" role="img" aria-label="Emblem of two wine glasses clinking with rising bubbles"></div>
      <h1 class="variety">MERLOT / CABERNET</h1>
      <div class="rule"></div>
      <p class="location">PONTE VALDORA</p>
      <p class="vintage">2016</p>
    </section>

    <div class="label-light"></div>

    <section class="light">
      <div class="emblem emblem--light" role="img" aria-label="Emblem of two wine glasses clinking with rising bubbles"></div>
      <h2 class="variety">MERLOT / CABERNET</h2>
      <div class="rule"></div>
      <p class="location">PONTE VALDORA</p>
      <p class="vintage">2016</p>
    </section>
  </main>
</body>
</html>
```